HVAC varko Hauler design New company

For my van wrap, 2016 Varko hauler medium roof work van for HVAC. the design should feature Quillmont Heating and Air Conditioning branding prominently, with a modern and professional look. The van should have a color scheme according to the uploaded files, with warm red/orange accents to symbolize heating. The company logo will be large and visible on both side panels and the rear, with clear contact details (555.014.2297, qmhvac.net) and a call to action like "Call for a Free Quote!"
Additional elements will include graphics like airflow lines, snowflakes, and sun symbols to represent your HVAC services Just like with my logo design. The text should highlight key services (heating, cooling, installation, repair) and a tagline like, "Mastering the elements of comfort!".
HVAC

```html
<!DOCTYPE html>
<html lang="en">
<head>
<meta charset="utf-8">
<title>Quillmont Heating &amp; Air Conditioning – Van Wrap Side Panel</title>
<link rel="stylesheet" href="https://fonts.googleapis.com/css2?family=Exo+2:wght@500&family=Open+Sans:wght@700;800&display=swap">
<style>
  :root {
    --wrap-red: #e8321f;
    --wrap-orange: #f26a1b;
    --flame-gold: #f7a21c;
    --accent-yellow: #f2e11a;
    --wrap-white: #f4f5f6;
    --cool-blue: #1f5fc4;
    --ice-blue: #5f9ee6;
    --logo-blue: #1d8fd8;
    --cta-blue: #1f5bc2;
    --page-bg: #ffffff;
  }
  html, body {
    margin: 0;
    padding: 0;
    width: 1200px;
    height: 797px;
    overflow: hidden;
    background: var(--page-bg);
  }
  .canvas {
    position: relative;
    width: 1200px;
    height: 797px;
  }
  .wrap-panel {
    position: absolute;
    left: 50px;
    top: 160px;
    width: 1100px;
    height: 480px;
    border-radius: 18px;
    overflow: hidden;
    background: var(--wrap-white);
  }
  .wrap-art {
    position: absolute;
    inset: 0;
    width: 1100px;
    height: 480px;
  }
  .brand-lockup {
    position: absolute;
    left: 440px;
    top: 262px;
    transform: rotate(-16deg);
    transform-origin: left top;
    font-family: "Exo 2", sans-serif;
    font-weight: 500;
    white-space: nowrap;
  }
  .brand-name {
    font-size: 56px;
    letter-spacing: 18px;
    line-height: 1;
    color: var(--logo-blue);
  }
  .brand-trade {
    margin-top: 8px;
    margin-left: 80px;
    font-size: 14px;
    letter-spacing: 8px;
    color: var(--wrap-red);
  }
  .contact {
    position: absolute;
    left: 728px;
    top: 300px;
    transform: rotate(-16deg);
    transform-origin: left top;
    font-family: "Open Sans", sans-serif;
    font-weight: 800;
    color: var(--wrap-red);
    text-align: right;
    line-height: 0.95;
  }
  .contact-phone { font-size: 42px; }
  .contact-web { font-size: 38px; }
  .quote-callout {
    position: absolute;
    left: 200px;
    top: 375px;
    width: 160px;
    text-align: center;
    font-family: "Open Sans", sans-serif;
    font-weight: 700;
    color: var(--cta-blue);
  }
  .quote-lead { font-size: 14px; line-height: 1.1; }
  .quote-banner {
    position: relative;
    margin: 2px auto 0;
    width: 150px;
    height: 30px;
    background: var(--wrap-red);
    clip-path: polygon(0 0, 100% 0, 88% 100%, 10% 100%);
    color: #fff;
    font-size: 25px;
    font-weight: 800;
    line-height: 30px;
  }
  .quote-tail { font-size: 14px; line-height: 1.2; }
</style>
</head>
<body>
<main class="canvas">
  <section class="wrap-panel" aria-label="Quillmont Heating and Air Conditioning van wrap side panel">
    <svg class="wrap-art" viewBox="0 0 1100 480" xmlns="http://www.w3.org/2000/svg">
      <defs>
        <linearGradient id="flameGlow" x1="0" y1="1" x2="1" y2="0">
          <stop offset="0" stop-color="#e8321f"/>
          <stop offset="0.55" stop-color="#f26a1b"/>
          <stop offset="1" stop-color="#f7a21c"/>
        </linearGradient>
        <linearGradient id="frostGlow" x1="0" y1="1" x2="1" y2="0">
          <stop offset="0" stop-color="#2a66c8"/>
          <stop offset="1" stop-color="#8fbdf0"/>
        </linearGradient>
      </defs>
      <path class="heat-field" d="M0 0 H1100 V22 C980 30 900 70 820 110 C700 170 520 200 380 240 C240 280 120 320 0 340 Z" fill="var(--wrap-red)"/>
      <path class="heat-flames" role="img" aria-label="Stylised orange flame illustration" d="M440 222 C530 150 590 60 650 10 L1060 10 C1020 40 960 55 900 72 C820 105 720 155 600 192 C545 207 490 216 440 222 Z" fill="url(#flameGlow)" opacity="0.85"/>
      <path class="heat-edge" d="M0 340 C120 320 240 280 380 240 C520 200 700 170 820 110 C900 70 980 30 1100 22" fill="none" stroke="var(--accent-yellow)" stroke-width="3"/>
      <path class="cool-field" d="M380 420 L1030 210 L1100 215 V420 Z" fill="var(--cool-blue)"/>
      <path class="cool-frost" role="img" aria-label="Frosted snowflake pattern" d="M700 312 L1030 210 L1100 215 V420 L760 420 Z" fill="url(#frostGlow)" opacity="0.8"/>
      <rect class="rocker-stripe" x="0" y="440" width="1100" height="26" fill="var(--cool-blue)"/>
    </svg>

    <div class="brand-lockup">
      <div class="brand-name">QUILLMONT</div>
      <div class="brand-trade">HEATING &amp; AIR CONDITIONING</div>
    </div>

    <div class="contact">
      <div class="contact-phone">555.014.2297</div>
      <div class="contact-web">qmhvac.net</div>
    </div>

    <div class="quote-callout">
      <div class="quote-lead">CALL FOR A</div>
      <div class="quote-banner">FREE</div>
      <div class="quote-tail">QUOTE!</div>
    </div>
  </section>
</main>
</body>
</html>
```